Business Card and Letterhead Design for Public Accounting Firm

Business card and letterhead design for a CPA Firm located in Orange County, CA. We're looking for a modern and professional design utilizing our existing logo. We'd like a clean "less is more" look, but also something that catches the eye. We provide a high level of service to our clients. Open to single or double sided business cards.

Additional info: color numbers on logo
Blue :
R 0
G 83
B 125

#00537D

Silver :

R 154
G 154
B 154

#9A9A9A

Target Market(s)

Businesses and individuals

Industry/Entity Type

Accounting

Contact Information for Business Card

Moss Whitfield & Danby LLP - 4827 Larkspur Vale Road, Irvine, CA 92614 - (949)731-2864 - mwdaccts.example

Font styles to use
Serif
Sans Serif
Other font styles liked:
• See font file uploaded

Colors
0054AA
0677BA
7BADD7
CADEEF
E8F1F8

Requirements
Nice to have
• Possibly use the font file provided which matches our logo, but adjust to be not in all caps

```html
<!DOCTYPE html>
<html lang="en">
<head>
<meta charset="utf-8">
<title>Moss Whitfield &amp; Danby LLP — Business Card</title>
<link rel="stylesheet" href="https://fonts.googleapis.com/css2?family=Libre+Baskerville:wght@400&family=Cormorant+Garamond:wght@500&display=swap">
<style>
  :root {
    --backdrop: #5c5d60;
    --card-white: #ffffff;
    --brand-blue: #1f6493;
    --brand-blue-deep: #00537d;
    --wave-blue: #2e6f9e;
    --silver: #9a9a9a;
    --silver-pale: #e6e8ea;
    --ink: #6a6c70;
    --rule: #d2d4d6;
    --mark-pale: #b9c4d6;
  }
  * { margin: 0; padding: 0; box-sizing: border-box; }
  html, body {
    width: 1200px; height: 859px; overflow: hidden;
    background: var(--backdrop);
  }
  .canvas {
    position: relative; width: 1200px; height: 859px;
  }
  .card {
    position: absolute; top: 292px;
    width: 480px; height: 274px;
    border-radius: 2px;
    overflow: hidden;
    box-shadow: 0 10px 24px rgba(0,0,0,.35);
  }
  .card--front { left: 90px; background: var(--card-white); }
  .card--back  { left: 630px; background: var(--wave-blue);
    display: flex; align-items: center; justify-content: center; }

  .card__wave { position: absolute; inset: 0; width: 480px; height: 274px; }

  .ghost-mark {
    position: absolute; right: 22px; top: 66px;
    font-family: "Cormorant Garamond", serif; font-weight: 500;
    font-size: 46px; color: var(--silver-pale); line-height: 1;
  }

  .brand {
    position: absolute; left: 28px; top: 50px;
    display: flex; align-items: center;
  }
  .brand__mark {
    font-family: "Cormorant Garamond", serif; font-weight: 500;
    font-size: 34px; color: var(--brand-blue); line-height: 1;
    padding-right: 10px; border-right: 1px solid var(--silver);
  }
  .brand__name {
    padding-left: 10px;
    font-family: "Libre Baskerville", serif; font-size: 10px;
    letter-spacing: 1.8px; text-transform: uppercase;
    color: var(--silver); line-height: 1.35;
  }

  .contact {
    position: absolute; left: 28px; top: 112px; width: 240px;
    list-style: none;
    font-family: "Libre Baskerville", serif; font-size: 11px;
    color: var(--ink); line-height: 1.45;
  }
  .contact__item {
    display: flex; gap: 6px;
    padding: 7px 0;
    border-top: 1px solid var(--rule);
  }
  .contact__label { color: var(--brand-blue); width: 16px; flex: none; }

  .back-mark {
    font-family: "Cormorant Garamond", serif; font-weight: 500;
    font-size: 96px; color: var(--mark-pale); line-height: 1;
  }
</style>
</head>
<body>
<main class="canvas">

  <section class="card card--front" aria-label="Business card front">
    <div class="ghost-mark" aria-hidden="true">MW&amp;D</div>

    <svg class="card__wave" viewBox="0 0 480 274" aria-hidden="true">
      <path d="M130,274 C260,250 300,240 480,232 L480,274 Z" fill="#f1f2f3"/>
      <path d="M110,274 C250,236 300,228 480,222 L480,230 C300,236 250,246 140,274 Z" fill="#e3e5e7"/>
      <path d="M480,40 C390,26 340,52 312,120 C285,190 250,248 160,274 L182,274
               C272,250 305,196 330,128 C356,62 400,50 480,56 Z" fill="var(--wave-blue)"/>
    </svg>

    <header class="brand">
      <div class="brand__mark">MW&amp;D</div>
      <div class="brand__name">Moss Whitfield<br>&amp; Danby LLP</div>
    </header>

    <ul class="contact">
      <li class="contact__item">
        <span class="contact__label">L:</span>
        <span>4827 Larkspur Vale Road,<br>Irvine, CA 92614</span>
      </li>
      <li class="contact__item">
        <span class="contact__label">P:</span>
        <span>(949)731-2864</span>
      </li>
      <li class="contact__item">
        <span class="contact__label">W:</span>
        <span>mwdaccts.example</span>
      </li>
    </ul>
  </section>

  <section class="card card--back" aria-label="Business card back">
    <div class="back-mark">MW&amp;D</div>
  </section>

</main>
</body>
</html>
```